Wordpress design for lovely french B&B - Mas des Tilleuls

We need a Wordpress design for a B&B located in eastern France.
The current website (designed by the previous owners) is here: http://www.masdestilleuls-exemple.fr. But it's not what we want, it has some photos so you can have a look at what it looks like.
New photos will be taken.

The new design should be fresh, modern and engaging and reflect the fact that it is a lovely B&B with 5 rooms. It is located in a lovely french village, close to the german and swiss border. It is perfectly located, close to the city, stores and highways, and also close to the country side.

The website should be able to describe each of the 5 rooms (1 page per room, with photos, description, price and booking).
The website should also have a pages to display the surrounding activities (one page with country side activities and one page with city activities) and also have a map for directions as well as a contact page with a form.
We will include a wordpress booking plugin so people can book online.

Target Market(s)

People visiting the french country side

Industry/Entity Type

Online

Logo Text

Le Mas des Tilleuls

Font styles to use
Script

Requirements
Must have
• Should feel like it's in the country side, but also feel like it's a little bit of luxury but not too much
Should not have
• I used B&B term to make it understandable, but it should not use the term B&B. It should use the french term "Gîte"

```html
<!DOCTYPE html>
<html lang="fr">
<head>
<meta charset="utf-8">
<title>Le Mas des Tilleuls</title>
<link href="https://fonts.googleapis.com/css2?family=Open+Sans:wght@400;600;700&display=swap" rel="stylesheet">
<style>
:root{
  --green:#1d6b36;
  --green-dark:#134f26;
  --green-deep:#0f4220;
  --green-light:#2f8a4a;
  --grey-bg:#eeeeee;
  --text:#555;
  --white:#fff;
  --footer-text:#d4e6d8;
}
*{box-sizing:border-box;margin:0;padding:0}
html,body{width:1200px;height:2800px;overflow:hidden}
body{font-family:"Open Sans",Arial,sans-serif;color:var(--text);background:var(--white);font-size:14px}
.topbar{height:64px;background:var(--green-dark);display:flex;align-items:center;justify-content:space-between;padding:0 140px}
.logo{color:var(--white);font-size:24px;font-weight:600;display:flex;align-items:center;gap:10px}
.logo-dot{width:12px;height:12px;border-radius:50%;background:var(--white)}
.topbar-right{display:flex;align-items:center;gap:24px}
.phone{color:var(--white);font-size:22px;font-weight:700;display:flex;align-items:center;gap:8px}
.search{width:200px;height:30px;background:var(--white);display:flex;align-items:center;justify-content:space-between;padding:0 10px;color:#999;font-size:12px}
.nav{height:48px;background:var(--white);display:flex;align-items:center;padding:0 120px;border-bottom:1px solid #ddd}
.nav a{color:var(--green);font-size:13px;font-weight:600;text-decoration:none;padding:15px 22px;text-transform:uppercase}
.nav a.active{background:var(--green);color:var(--white)}
.hero{position:relative;height:610px}
.hero-photo{position:absolute;inset:0;background:linear-gradient(120deg,#6d5a49 0%,#b9a690 35%,#e6ddd0 60%,#a58a6c 100%)}
.hero-caption{position:absolute;left:120px;top:190px;width:420px;background:rgba(255,255,255,.85);padding:24px 28px}
.hero-caption h1{color:var(--green);font-size:36px;font-weight:700;margin-bottom:10px}
.hero-caption p{font-size:14px;line-height:1.5;color:#444}
.booking{position:absolute;right:120px;top:30px;width:290px;background:rgba(15,66,32,.9);padding:18px 20px;color:var(--white)}
.booking h2{font-size:28px;font-weight:700;margin-bottom:12px}
.booking label{display:block;font-size:11px;margin:8px 0 3px}
.booking .field{height:26px;background:var(--white)}
.booking .row{display:flex;gap:10px}
.booking .row>div{flex:1}
.booking .btn{margin-top:16px;height:32px;background:var(--green-light);display:flex;align-items:center;justify-content:center;font-size:13px;font-weight:600}
.dots{position:absolute;bottom:20px;left:50%;transform:translateX(-50%);display:flex;gap:8px}
.dots span{width:9px;height:9px;border-radius:50%;background:rgba(255,255,255,.6)}
.dots span:first-child{background:var(--white)}
.intro{height:420px;padding-top:46px;text-align:center}
.intro h2{color:var(--green);font-size:30px;font-weight:600}
.intro .lead{font-size:14px;margin:10px 0 34px}
.features{display:flex;align-items:center;justify-content:center;gap:22px}
.arrow{color:var(--green);font-size:28px;font-weight:700;width:30px}
.feature{width:290px;height:130px;background:var(--green);color:var(--white);font-size:14px;line-height:1.5;display:flex;align-items:center;justify-content:center;padding:20px;text-align:center}
.philo{width:960px;margin:20px auto 0;text-align:right;font-size:13px}
.philo b{color:var(--green)}
.activities{height:760px;background:var(--grey-bg);padding:40px 120px;display:flex;gap:40px}
.act-col{flex:1}
.act-head{display:flex;justify-content:space-between;align-items:center;border-bottom:1px solid #ccc;padding-bottom:12px;margin-bottom:24px}
.act-head h2{color:var(--green);font-size:30px;font-weight:600}
.act-head .arrows{color:var(--green);font-size:20px;font-weight:700;letter-spacing:10px}
.act-grid{display:grid;grid-template-columns:repeat(3,1fr);gap:40px 20px}
.card-img{height:130px}
.card h3{color:var(--green);font-size:17px;font-weight:700;margin:12px 0 6px}
.card p{font-size:12px;line-height:1.5}
.card .btn{display:inline-block;margin-top:12px;background:var(--green);color:var(--white);font-size:12px;font-weight:600;padding:7px 14px}
.lower{height:540px;padding:40px 120px;display:flex;gap:50px}
.gallery{width:540px}
.lower h2{color:var(--green);font-size:30px;font-weight:600;border-bottom:1px solid #ccc;padding-bottom:12px;margin-bottom:22px}
.gallery-frame{position:relative;height:380px}
.gallery-img{position:absolute;inset:0;background:linear-gradient(160deg,#6f8f55,#a9b98c 45%,#d7d2c4 70%,#4f6b3a)}
.gallery-frame .g-arrow{position:absolute;top:45%;color:var(--white);font-size:34px;font-weight:700}
.gallery-frame .left{left:14px}.gallery-frame .right{right:14px}
.gallery-caption{position:absolute;left:0;right:0;bottom:0;height:60px;background:var(--green);color:var(--white);padding:0 24px;display:flex;align-items:center;font-size:14px}
.news{flex:1}
.news-item{display:flex;gap:20px;margin-bottom:34px}
.news-img{width:180px;height:140px;flex:none}
.news-item h3{color:var(--green);font-size:17px;font-weight:700;margin-bottom:8px}
.news-item p{font-size:14px;line-height:1.5}
.news-item a{color:var(--green);font-weight:600;text-decoration:none}
.footer{height:358px;background:var(--green-deep);color:var(--white);padding:30px 120px 0}
.footer-cols{display:flex;gap:40px;height:220px}
.footer-col{width:160px}
.footer h4{font-size:13px;font-weight:700;text-transform:uppercase;margin-bottom:10px}
.footer li{list-style:none;font-size:12px;line-height:1.7;color:var(--footer-text)}
.footer-map{flex:1}
.footer-map .map{height:150px;background:linear-gradient(135deg,#d9dccf,#eceee4 50%,#c9d3bc)}
.footer-bottom{display:flex;align-items:center;justify-content:space-between;border-top:1px solid rgba(255,255,255,.2);padding-top:20px;font-size:12px;color:var(--footer-text)}
.footer-bottom .left{display:flex;align-items:center;gap:16px}
.badge{width:40px;height:40px;border-radius:50%;background:#e0c76a}
.badge.sq{border-radius:4px;background:#f4f4f4}
.social{display:flex;align-items:center;gap:8px}
.social span.c{width:24px;height:24px;border-radius:50%;border:1px solid var(--white)}
</style>
</head>
<body>
<header class="topbar">
  <div class="logo"><span class="logo-dot"></span>Le Mas des Tilleuls</div>
  <div class="topbar-right">
    <div class="phone">
      <svg width="20" height="20" viewBox="0 0 24 24"><path fill="#fff" d="M6.6 10.8a15 15 0 0 0 6.6 6.6l2.2-2.2c.3-.3.7-.4 1-.2 1.1.4 2.3.6 3.6.6.6 0 1 .4 1 1V20c0 .6-.4 1-1 1A17 17 0 0 1 3 4c0-.6.4-1 1-1h3.5c.6 0 1 .4 1 1 0 1.3.2 2.5.6 3.6.1.3 0 .7-.2 1z"/></svg>
      +33 6 12 34 56 78
    </div>
    <div class="search">Search
      <svg width="14" height="14" viewBox="0 0 24 24"><circle cx="10" cy="10" r="7" fill="none" stroke="#777" stroke-width="2"/><path d="M15 15l6 6" stroke="#777" stroke-width="2"/></svg>
    </div>
  </div>
</header>
<nav class="nav">
  <a class="active">Home</a><a>Photos</a><a>Price</a><a>Booking</a><a>Country Activities</a><a>City Activities</a><a>Map</a><a>Contact</a>
</nav>

<section class="hero">
  <div class="hero-photo" role="img" aria-label="Breakfast table with teapot and open book in a guest room"></div>
  <div class="hero-caption">
    <h1>Le Mas des Tilleuls</h1>
    <p>C'est une maison du XVIIe siècle entièrement rénovée, au cœur du village, à proximité immédiate des commerces, de la ville et des restaurants.</p>
  </div>
  <div class="booking">
    <h2>Booking Online</h2>
    <label>Hotel</label><div class="field"></div>
    <label>Check-in date</label><div class="field"></div>
    <label>Check-out date</label><div class="field"></div>
    <div class="row">
      <div><label>Rooms</label><div class="field"></div></div>
      <div><label>Guest</label><div class="field"></div></div>
    </div>
    <div class="btn">SEARCH</div>
  </div>
  <div class="dots"><span></span><span></span><span></span><span></span></div>
</section>

<section class="intro">
  <h2>Le Mas des Tilleuls</h2>
  <p class="lead">Welcomes you and offers a quality service for your needs</p>
  <div class="features">
    <span class="arrow">&#8249;</span>
    <div class="feature">Town side, the large porch, study, the enclosed courtyard of this solid building</div>
    <div class="feature">Garden, a mulberry tree over a century gives the place its name</div>
    <div class="feature">Wide, the five apartments with exposed beams, antique furniture and a thousand and one details</div>
    <span class="arrow">&#8250;</span>
  </div>
  <p class="philo"><b>Notre philosophie :</b> Vous satisfaire tout au long de votre séjour.</p>
</section>

<section class="activities">
  <div class="act-col">
    <div class="act-head"><h2>Country Activities</h2><span class="arrows">&#8249;&#8250;</span></div>
    <div class="act-grid">
      <div class="card"><div class="card-img" role="img" aria-label="Illuminated town square at night" style="background:linear-gradient(135deg,#3a3f6b,#b0724a)"></div><h3>February 2015</h3><p>Neque porro quisquam est qui dolorem ipsum quia dolor sit amet</p><span class="btn">View Details</span></div>
      <div class="card"><div class="card-img" role="img" aria-label="Old timbered village houses" style="background:linear-gradient(135deg,#9fb0c8,#c9a27a)"></div><h3>February 2015</h3><p>Neque porro quisquam est qui dolorem ipsum quia dolor sit amet</p><span class="btn">View Details</span></div>
      <div class="card"><div class="card-img" role="img" aria-label="Canal lined with houses" style="background:linear-gradient(135deg,#8fb1d0,#7a8f5a)"></div><h3>February 2015</h3><p>Neque porro quisquam est qui dolorem ipsum quia dolor sit amet</p><span class="btn">View Details</span></div>
      <div class="card"><div class="card-img" role="img" aria-label="Rows of colourful wine bottles" style="background:linear-gradient(135deg,#5a2f3a,#c8864a)"></div><h3>February 2015</h3><p>Neque porro quisquam est qui dolorem ipsum quia dolor sit amet</p><span class="btn">View Details</span></div>
      <div class="card"><div class="card-img" role="img" aria-label="Historic church in the village" style="background:linear-gradient(135deg,#9db6d4,#b49878)"></div><h3>February 2015</h3><p>Neque porro quisquam est qui dolorem ipsum quia dolor sit amet</p><span class="btn">View Details</span></div>
      <div class="card"><div class="card-img" role="img" aria-label="Riverside houses under a blue sky" style="background:linear-gradient(135deg,#7ea6d2,#9a7a5e)"></div><h3>February 2015</h3><p>Neque porro quisquam est qui dolorem ipsum quia dolor sit amet</p><span class="btn">View Details</span></div>
    </div>
  </div>
  <div class="act-col">
    <div class="act-head"><h2>City Activities</h2><span class="arrows">&#8249;&#8250;</span></div>
    <div class="act-grid">
      <div class="card"><div class="card-img" role="img" aria-label="City square with a statue" style="background:linear-gradient(135deg,#9fbde0,#a98a6a)"></div><h3>February 2015</h3><p>Neque porro quisquam est qui dolorem ipsum quia dolor sit amet</p><span class="btn">View Details</span></div>
      <div class="card"><div class="card-img" role="img" aria-label="Palm lined avenue" style="background:linear-gradient(135deg,#8ab5e0,#6f8a4e)"></div><h3>February 2015</h3><p>Neque porro quisquam est qui dolorem ipsum quia dolor sit amet</p><span class="btn">View Details</span></div>
      <div class="card"><div class="card-img" role="img" aria-label="City street with shops" style="background:linear-gradient(135deg,#a8c0dc,#8a7d6c)"></div><h3>February 2015</h3><p>Neque porro quisquam est qui dolorem ipsum quia dolor sit amet</p><span class="btn">View Details</span></div>
      <div class="card"><div class="card-img" role="img" aria-label="Colourful city facades" style="background:linear-gradient(135deg,#d49a5a,#7b8fae)"></div><h3>February 2015</h3><p>Neque porro quisquam est qui dolorem ipsum quia dolor sit amet</p><span class="btn">View Details</span></div>
      <div class="card"><div class="card-img" role="img" aria-label="Market square with buildings" style="background:linear-gradient(135deg,#c7a27c,#8aa7c9)"></div><h3>February 2015</h3><p>Neque porro quisquam est qui dolorem ipsum quia dolor sit amet</p><span class="btn">View Details</span></div>
      <div class="card"><div class="card-img" role="img" aria-label="Boulevard with trees" style="background:linear-gradient(135deg,#90b2d8,#6a7f52)"></div><h3>February 2015</h3><p>Neque porro quisquam est qui dolorem ipsum quia dolor sit amet</p><span class="btn">View Details</span></div>
    </div>
  </div>
</section>

<section class="lower">
  <div class="gallery">
    <h2>Photo Gallery</h2>
    <div class="gallery-frame">
      <div class="gallery-img" role="img" aria-label="Garden terrace with table, chairs and stone wall"></div>
      <span class="g-arrow left">&#8249;</span><span class="g-arrow right">&#8250;</span>
      <div class="gallery-caption">Neque porro quisquam est qui dolorem ipsum quia dolor sit amet</div>
    </div>
  </div>
  <div class="news">
    <h2>Latest News</h2>
    <div class="news-item">
      <div class="news-img" role="img" aria-label="Bright guest bedroom" style="background:linear-gradient(135deg,#e8e0d2,#a88b6c)"></div>
      <div><h3>25th February 2015</h3><p>Neque porro quisquam est qui dolorem ipsum quia dolor sit amet, consectetur, adipisci velit.... <a>Read More</a></p></div>
    </div>
    <div class="news-item">
      <div class="news-img" role="img" aria-label="Cosy sitting room" style="background:linear-gradient(135deg,#d8cdb8,#8c6f52)"></div>
      <div><h3>25th February 2015</h3><p>Neque porro quisquam est qui dolorem ipsum quia dolor sit amet, consectetur, adipisci velit.... <a>Read More</a></p></div>
    </div>
  </div>
</section>

<footer class="footer">
  <div class="footer-cols">
    <div class="footer-col"><h4>Menu Links</h4><ul><li>Home</li><li>Photos</li><li>Price</li><li>Booking</li><li>Country Activities</li><li>City Activities</li><li>Map</li><li>Contact</li></ul></div>
    <div class="footer-col"><h4>Other Links</h4><ul><li>Terms Of Service</li><li>Privacy Policy</li><li>Cookies</li></ul></div>
    <div class="footer-col" style="width:220px"><h4>Contact Us</h4><ul><li><b>Le Mas des Tilleuls</b></li><li>14 rue des Vergers</li><li>68000 Village</li><li>Téléphone : +33 6 12 34 56 78</li><li>contact@masdestilleuls-exemple.fr</li></ul></div>
    <div class="footer-map"><h4>Map</h4><div class="map" role="img" aria-label="Street map showing the location of the gîte"></div></div>
  </div>
  <div class="footer-bottom">
    <div class="left">Certifié membre du Réseau des Séjours Verts<span class="badge sq"></span><span class="badge"></span></div>
    <div class="social">Follow Us<span class="c"></span><span class="c"></span><span class="c"></span><span class="c"></span></div>
  </div>
</footer>
</body>
</html>
```